Business Card for Professional Photographer

I'm looking for an eye catching modern clean design that compliments my logo/ website fonts & colours.
I specialise in architecture, corporate & commercial photography so I'm marketing to professional clients rather than portrait / wedding clients.

I would prefer to not have a solid black design.

My logo brand guide is as follows :

Main front font. : Reislust
Main font colour : #fff
Slogan front font : Ubuntu Bold
Monogram front font : Venti Medium
Container colour : #fff

I need print ready files in pdf .png & .eps formats.

Included in the files below are some screen grabs as reference to font & colours etc.

```html
<!DOCTYPE html>
<html lang="en">
<head>
<meta charset="utf-8">
<title>Frameline Studio – Business Card</title>
<link rel="stylesheet" href="https://fonts.googleapis.com/css2?family=Ubuntu:wght@300;400;700&family=Roboto:wght@400&display=swap">
<style>
  :root {
    --page: #e6e6e6;
    --ink: #17181b;
    --gold: #d6ad5c;
    --white: #ffffff;
  }
  * { box-sizing: border-box; margin: 0; padding: 0; }
  html, body { width: 799px; height: 1200px; overflow: hidden; }
  body {
    background: var(--page);
    font-family: "Ubuntu", sans-serif;
    position: relative;
  }
  .card {
    position: absolute;
    left: 60px;
    width: 680px;
    height: 390px;
    border-radius: 4px;
    overflow: hidden;
    box-shadow: 0 10px 28px rgba(0,0,0,.28);
  }
  .card--front { top: 120px; background: var(--ink); }
  .card--back { top: 690px; background: var(--ink); }

  /* front */
  .front__gallery {
    position: absolute; inset: 0;
    background:
      linear-gradient(90deg, transparent 0 30%, rgba(0,0,0,.25) 30% 30.6%, transparent 30.6% 62%, rgba(0,0,0,.25) 62% 62.6%, transparent 62.6%),
      linear-gradient(135deg, #2a2f36 0%, #1d1f24 40%, #2b2a28 70%, #1a1c20 100%);
  }
  .front__brand {
    position: absolute; left: 90px; top: 130px;
    display: flex; align-items: center; gap: 22px;
  }
  .brand__dot {
    display: block;
    width: 70px; height: 70px; border-radius: 50%;
    background: var(--gold);
    flex: none;
  }
  .brand__name {
    font-weight: 300; font-size: 38px; letter-spacing: 6px;
    color: var(--gold); text-transform: uppercase;
    white-space: nowrap;
  }
  .brand__tagline {
    font-weight: 300; font-size: 14px; letter-spacing: 3px;
    color: var(--gold); margin-top: 6px;
    white-space: nowrap;
  }
  .front__web {
    position: absolute; left: 182px; top: 280px;
    font-weight: 300; font-size: 17px; letter-spacing: 3px;
    color: var(--gold);
  }

  /* back */
  .back__wave { position: absolute; inset: 0; width: 680px; height: 390px; }
  .back__brand {
    position: absolute; left: 48px; top: 32px;
  }
  .back__brand .brand__dot { width: 40px; height: 40px; margin-bottom: 10px; }
  .back__brand .brand__name { color: var(--white); font-size: 28px; letter-spacing: 5px; }
  .back__brand .brand__tagline { font-size: 11px; letter-spacing: 2.5px; margin-top: 4px; }
  .person {
    position: absolute; right: 48px; top: 112px; text-align: right;
  }
  .person__name { font-weight: 700; font-size: 22px; color: var(--gold); }
  .person__role { font-weight: 400; font-size: 17px; color: var(--white); margin-top: 2px; }
  .contact {
    position: absolute; right: 40px; top: 266px;
    list-style: none;
    font-family: "Roboto", sans-serif; font-size: 17px; color: var(--ink);
  }
  .contact li {
    display: flex; justify-content: flex-end; align-items: center;
    gap: 12px; height: 26px; white-space: nowrap;
  }
  .contact svg { width: 16px; height: 16px; fill: var(--ink); flex: none; }
  .contact .no-icon { display: block; width: 16px; flex: none; }
</style>
</head>
<body>

<section class="card card--front">
  <div class="front__gallery" role="img" aria-label="Dimmed collage of architecture and commercial photographs"></div>
  <div class="front__brand">
    <span class="brand__dot"></span>
    <div>
      <div class="brand__name">Frameline Studio</div>
      <div class="brand__tagline">Architecture Corporate Commercial</div>
    </div>
  </div>
  <div class="front__web">www.framelinestudio.com.au</div>
</section>

<section class="card card--back">
  <svg class="back__wave" viewBox="0 0 680 390" preserveAspectRatio="none" aria-hidden="true">
    <defs>
      <linearGradient id="goldFill" x1="0" y1="0" x2="1" y2="1">
        <stop offset="0" stop-color="#f6e3a4"/>
        <stop offset=".5" stop-color="#e3c57a"/>
        <stop offset="1" stop-color="#f2dc9c"/>
      </linearGradient>
      <linearGradient id="goldBand" x1="0" y1="0" x2="1" y2="0">
        <stop offset="0" stop-color="#f3dc98"/>
        <stop offset=".5" stop-color="#c8963f"/>
        <stop offset="1" stop-color="#a97a2c"/>
      </linearGradient>
    </defs>
    <path d="M0 160 C120 150 230 195 340 212 C460 230 570 205 680 170 L680 390 L0 390 Z" fill="url(#goldBand)"/>
    <path d="M0 174 C130 168 235 208 345 224 C465 239 575 216 680 182 L680 390 L0 390 Z" fill="#1a1b1e"/>
    <path d="M0 188 C140 186 240 222 352 234 C470 245 580 226 680 194 L680 390 L0 390 Z" fill="url(#goldBand)"/>
    <path d="M0 200 C150 202 250 234 360 243 C480 251 590 234 680 206 L680 390 L0 390 Z" fill="url(#goldFill)"/>
  </svg>

  <div class="back__brand">
    <span class="brand__dot"></span>
    <div class="brand__name">Frameline Studio</div>
    <div class="brand__tagline">Architecture Corporate Commercial</div>
  </div>

  <div class="person">
    <div class="person__name">Mara Ellison</div>
    <div class="person__role">Photographer</div>
  </div>

  <ul class="contact">
    <li>0412555018
      <svg viewBox="0 0 16 16"><path d="M3 1h3l1.5 4-2 1.2a9 9 0 0 0 4.3 4.3L11 8.5l4 1.5v3a2 2 0 0 1-2 2A12 12 0 0 1 1 3a2 2 0 0 1 2-2z"/></svg>
    </li>
    <li>framelinestudio.com.au
      <svg viewBox="0 0 16 16"><path d="M1 3h14v10H1z M1 3l7 6 7-6" fill="none" stroke="#17181b" stroke-width="1.5"/></svg>
    </li>
    <li>hello@framelinestudio.com.au
      <svg viewBox="0 0 16 16"><circle cx="8" cy="8" r="6.5" fill="none" stroke="#17181b" stroke-width="1.4"/><path d="M1.5 8h13M8 1.5c-3 3.5-3 9.5 0 13M8 1.5c3 3.5 3 9.5 0 13" fill="none" stroke="#17181b" stroke-width="1.2"/></svg>
    </li>
    <li>48 Harbour Rd Lorne Vic 3232 <span class="no-icon"></span></li>
  </ul>
</section>

</body>
</html>
```